Business Card design for Property Developer

We need a business card design for a Melbourne based Property Developer called "Kestrelmoor Holdings Pty Ltd".

We subdivide land and onsell to builders etc.

We already have a company logo, which is attached. Also I have attached the layout requirements from the printer. We would like a 2-sided design with one side displaying our logo by itself and the other with the required info, such as name, address, tel no., email, abn etc. The card will need to be used by 4 members of staff so name and contact details should be interchangable.
Updates

If possible, can you please write "name' "job position" "phone" "email" "address" on the card but leave them so I can add the details at a later time. Thank you. Also I plan on printing with UV spot printing as a background on the card. Keep this is mind when designing.

Thanks again.

Hello designers, please do not include pics of houses, house plansĀ or construction machinery etc as we really do not like the way it looks. Thank you.

Target Market(s)

Real Estate Agents, Land Owners, Local Council Departments, Govt Bodies, other Developers etc.

Industry/Entity Type

Business

Requirements
Must have
• 2-sided design with one side displaying our logo by itself and the other with the required info, such as name, address, tel no., email, abn etc.

```html
<!DOCTYPE html>
<html lang="en">
<head>
<meta charset="utf-8">
<title>Kestrelmoor Holdings – Business Card</title>
<link rel="stylesheet" href="https://fonts.googleapis.com/css2?family=Roboto:wght@400;700;900&display=swap">
<style>
  :root {
    --page-bg: #ffffff;
    --red-bright: #ff0008;
    --red-deep: #8a0c08;
    --blue-dark: #1a4aa0;
    --blue-light: #1f8cbf;
    --blue-edge: #1565b0;
    --logo-red: #d10a0a;
    --logo-blue: #1b3f9e;
    --card-border: #b0452a;
    --white: #ffffff;
  }
  * { margin: 0; padding: 0; box-sizing: border-box; }
  html, body {
    width: 1200px; height: 900px; overflow: hidden;
    background: var(--page-bg);
    font-family: "Roboto", Arial, sans-serif;
  }
  .canvas { position: relative; width: 1200px; height: 900px; }

  .card-front {
    position: absolute; left: 35px; top: 277px;
    width: 546px; height: 355px;
    background: linear-gradient(90deg, var(--red-bright) 0%, #c30808 50%, var(--red-deep) 100%);
    color: var(--white);
  }
  .holder { position: absolute; right: 34px; top: 40px; text-align: right; }
  .holder-name { font-weight: 700; font-size: 23px; line-height: 28px; }
  .holder-role { font-weight: 400; font-size: 16px; line-height: 19px; margin-top: 4px; text-transform: uppercase; }

  .accent-bar {
    position: absolute; left: 0; height: 46px;
    background: linear-gradient(90deg, var(--blue-dark), var(--blue-light));
    border: 4px solid var(--blue-edge); border-left: none;
  }
  .accent-bar--long { top: 123px; width: 227px; }
  .accent-bar--short { top: 179px; width: 155px; }

  .company { position: absolute; right: 34px; top: 230px; text-align: right; }
  .company-name { font-weight: 700; font-size: 14.5px; line-height: 18px; text-transform: uppercase; }
  .company-details { font-size: 14.5px; line-height: 19px; margin-top: 2px; }
  .company-details .gap { display: inline-block; width: 10px; }

  .card-back {
    position: absolute; left: 618px; top: 278px;
    width: 546px; height: 356px;
    background: var(--white);
    border: 1px solid var(--card-border);
  }
  .brand {
    position: absolute; left: 0; right: 0; top: 78px;
    display: flex; flex-direction: column; align-items: center;
  }
  .brand-dot { width: 150px; height: 150px; border-radius: 50%; background: var(--logo-blue); }
  .brand-name {
    margin-top: 22px;
    font-weight: 900; font-size: 36px; line-height: 40px;
    color: var(--logo-red); text-transform: uppercase; letter-spacing: 0.5px;
  }
</style>
</head>
<body>
<main class="canvas">
  <section class="card-front" aria-label="Card front with contact details">
    <div class="holder">
      <p class="holder-name">First Lastname</p>
      <p class="holder-role">Founding Partner/Director of<br>Property Development</p>
    </div>
    <div class="accent-bar accent-bar--long"></div>
    <div class="accent-bar accent-bar--short"></div>
    <div class="company">
      <p class="company-name">Kestrelmoor Holdings Pty Ltd</p>
      <p class="company-details">
        01A, 98-76 Somename Street, Matchingname City 5432, Australia<br>
        Telephone: +61 3 9000 4410<span class="gap"></span>Facsimile: +61 3 9000 4420<br>
        Email: flastname@kestrelmoor.com.au<br>
        www.kestrelmoor.com.au
      </p>
    </div>
  </section>

  <section class="card-back" aria-label="Card back with company name">
    <div class="brand">
      <div class="brand-dot"></div>
      <p class="brand-name">Kestrelmoor Holdings</p>
    </div>
  </section>
</main>
</body>
</html>
```